FlockVault.net website design

We are looking for a design for a new website we are about to launch called FlockVault.net. FlockVault.net is an online discount wine site that will focus on selling only one wine at a time. (This potentially may become two or three wines at a time in the future but only one for now). The wine that is up for sale will not actually be sold until a pre-set number of buyers “the group” commits to buying the wine. If the threshold of buyers is not met then the wine is not sold. This group aspect is what makes the site unique. By only selling the wine when the group commits to buying it we are able to deliver them a great wine at a fantastic price.
The website should convey a fun feeling while also indicating that this is a place where serious wine enthusiasts can shop. We will be providing information, ratings, and reviews about the wines that are currently on sale.
Updates
Target Market(s)
The target market is a wide range of wine enthusiasts, from people in their 20s and 30s to more mature and serious wine connoisseurs.
Industry/Entity Type
Shop
Requirements
Must have
- Below is a list of specifications for the website:
1) Main page with our logo (which includes green, purple, and a magenta wine color) that showcases the current wine that's for sale
- The site’s main focus should be on selling ONE bottle of wine at a time at group rate.
- The site should capture the group buying concept as this is what differentiates our site from the others. Visitors to the site should get the sense that they are part of a special community that is getting a great deal because they are buying the wine as a group.
- A meter or better yet an animation should be used to indicate if the tipping point has been met for a sale. We’d like to see some creative ideas here.
- Nice high-res photo of the wine bottle
- Detailed description of what kind of wine it is, where the wine is from, type of grape, vino observer and other ratings, description of what it tastes like. We would like the option to provide as much detail here as possible.
- Breakdown on what the prices are per bottle and the discount we're giving. We would like to show the original price as compared to the FlockVault.net price.
- Potentially show a list of upcoming wines. Maybe not the exact wine that will be for sale next but some info to entice users to keep checking.
2) User Account Log in
- Ability to create and log into a personal account
The personal account should be able to:
-store users' credit card and shipping information as well as past orders
-allow you to opt in or out of flock vault emails
-potentially store wine preference or ratings information
-refer a friend option where you get some kind of incentive
3) The Group Concept. The website design must include a few aspects that identify FlockVault.net as a social site, not simply a wine sale site.
- Some kind of indicator showing if the group threshold has been met or not. We would like to see some type of animation with wine bottles filling up, or grapes on a scale-something that would change as the number of people buying into the sale increase.
- Button to join the group purchase
4) General Site Content must include:
- Email link to send questions to support
- Information on how shipping works and other FAQs
- Legal disclaimer
- Links to Facebook and Twitter
Nice to have
- It would be nice to have a discussion board where FlockVault members can discuss wines.
Should not have
- The design should not be for a general wine store that sells a variety of different wines.

```html
<!DOCTYPE html>
<html lang="en">
<head>
<meta charset="utf-8">
<title>FlockVault.net – Group wine buying</title>
<link rel="stylesheet" href="https://fonts.googleapis.com/css2?family=Arimo:wght@400;700&family=Reenie+Beanie&family=Sniglet:wght@800&display=swap">
<style>
  :root {
    --magenta: #c93f86;
    --magenta-light: #dc5198;
    --magenta-text: #cc2a78;
    --green: #8dc63f;
    --green-dark: #6da52a;
    --green-light: #b5dd6a;
    --grey-display: #8c8c8c;
    --grey-text: #8a8a8a;
    --ink: #111111;
    --red-price: #e0201c;
    --white: #ffffff;
    --wine: #3a1a1e;
  }
  * { margin: 0; padding: 0; box-sizing: border-box; }
  a { text-decoration: none; }
  html, body { width: 888px; height: 1200px; overflow: hidden; background: var(--white); }
  body { position: relative; font-family: "Arimo", Arial, sans-serif; color: var(--ink); }
  .abs { position: absolute; }

  /* Header */
  .site-header {
    position: absolute; left: 0; top: 0; width: 888px; height: 126px;
    background: linear-gradient(180deg, var(--magenta) 0%, var(--magenta-light) 100%);
  }
  .brand-card {
    position: absolute; left: 22px; top: 8px; width: 186px; height: 70px;
    background: var(--white); transform: rotate(-12deg);
    box-shadow: 2px 3px 6px rgba(0,0,0,.3);
    display: flex; align-items: center; gap: 8px; padding-left: 16px;
  }
  .brand-dot { width: 22px; height: 22px; border-radius: 50%; background: var(--green); flex: none; }
  .brand-name { font-family: "Arimo", sans-serif; font-weight: 700; font-size: 19px; color: var(--green-dark); }
  .headline {
    left: 257px; top: 22px; font-family: "Reenie Beanie", cursive;
    font-size: 30px; line-height: 36px; color: var(--white); white-space: nowrap;
  }
  .main-nav a {
    position: absolute; top: 100px; height: 26px; width: 66px;
    font-size: 9.5px; color: var(--ink);
    display: flex; align-items: center; justify-content: center;
    background: linear-gradient(180deg, var(--green-light), var(--green));
    border-radius: 3px 3px 0 0;
  }
  .main-nav a.is-active { background: var(--white); }
  .login-bar {
    left: 495px; top: 100px; width: 214px; height: 26px;
    background: linear-gradient(180deg, var(--green-light), var(--green));
    border-radius: 3px 3px 0 0; font-size: 9px; color: var(--white);
    display: flex; align-items: center; gap: 8px; padding-left: 22px;
  }
  .login-bar .field {
    width: 58px; height: 10px; background: var(--white); border-radius: 1px;
    font-size: 6px; color: #bbb; text-align: center; line-height: 10px;
  }
  .login-bar .field:first-of-type { margin-left: 12px; }

  /* Hero */
  .hero {
    left: 167px; top: 126px; width: 573px; height: 238px; background: var(--white);
    box-shadow: 0 6px 10px -6px rgba(0,0,0,.12), -6px 0 10px -8px rgba(0,0,0,.15), 6px 0 10px -8px rgba(0,0,0,.15);
  }
  .community-art {
    left: 230px; top: 160px; width: 182px; height: 165px;
    background: radial-gradient(circle, #dcebc4 0%, #eef4e6 60%, #ffffff 100%); border-radius: 50%;
  }
  .hero-title {
    left: 465px; top: 152px; font-family: "Sniglet", sans-serif; font-weight: 800; font-size: 36px;
    line-height: 33px; color: var(--grey-display); letter-spacing: -.5px;
  }
  .hero-lead { left: 464px; top: 265px; width: 250px; font-size: 11px; line-height: 14px; color: var(--magenta-text); }
  .btn-register {
    left: 509px; top: 305px; width: 157px; height: 48px; border-radius: 4px;
    background: linear-gradient(180deg, var(--green-light), var(--green-dark));
    font-family: "Sniglet", sans-serif; font-weight: 800; font-size: 21px; color: var(--white);
    display: flex; align-items: center; justify-content: center;
    box-shadow: 0 2px 3px rgba(0,0,0,.15);
  }

  /* Featured wine */
  .bottle-photo {
    left: 276px; top: 414px; width: 75px; height: 280px; border-radius: 14px 14px 8px 8px;
    background: linear-gradient(90deg, #1e0b0f 0%, var(--wine) 40%, #5a2a30 55%, #1e0b0f 100%);
  }
  .wine-name { left: 408px; top: 440px; font-size: 23px; font-weight: 700; letter-spacing: -.3px; }
  .wine-type { left: 409px; top: 467px; font-size: 14px; color: var(--magenta-text); }
  .price-tag { left: 495px; top: 434px; }
  .price-was { left: 538px; top: 450px; font-size: 12.5px; font-weight: 700; color: var(--red-price); }
  .price-label { left: 540px; top: 470px; font-weight: 700; font-size: 15px; color: var(--white); }
  .price-now { left: 563px; top: 484px; font-weight: 700; font-size: 23px; color: var(--white); }
  .wine-origin { left: 407px; top: 528px; width: 200px; font-size: 7.4px; line-height: 9.4px; color: var(--grey-text); }
  .wine-origin b { color: #777; }
  .articles-link { left: 405px; top: 594px; display: flex; align-items: center; gap: 12px; font-size: 9.5px; }
  .rating { left: 403px; top: 630px; }
  .meter-label { left: 409px; top: 673px; font-size: 10px; font-weight: 700; color: var(--magenta-text); }
  .buying-meter {
    left: 403px; top: 689px; width: 165px; height: 19px; border-radius: 3px;
    background: #6d6d6d; border: 2px solid #333;
  }
  .buying-meter span {
    display: block; width: 79%; height: 100%; border-radius: 2px;
    background: linear-gradient(180deg, var(--green-light), var(--green));
  }
  .btn-buy {
    left: 401px; top: 721px; width: 80px; height: 24px; border-radius: 2px;
    background: linear-gradient(180deg, var(--green-light), var(--green));
    font-size: 10px; font-weight: 700; color: var(--white);
    display: flex; align-items: center; justify-content: center;
  }
  .carousel-arrow { width: 32px; height: 42px; }

  /* How it works */
  .section-rule { left: 167px; top: 800px; width: 518px; height: 6px; background: linear-gradient(180deg, rgba(0,0,0,.08), rgba(0,0,0,0)); }
  .tab-how {
    left: 200px; top: 805px; width: 105px; height: 17px;
    background: linear-gradient(180deg, var(--green-light), var(--green));
    font-size: 9px; display: flex; align-items: center; padding-left: 18px;
  }
  .how-copy { left: 205px; top: 850px; width: 456px; font-size: 8.8px; line-height: 11.6px; }
  .how-copy h2 { font-size: 8.8px; font-weight: 700; margin-bottom: 10px; }
  .how-copy p { margin-bottom: 11px; }

  .social { left: 166px; top: 1119px; display: flex; gap: 5px; }
  .social span { width: 21px; height: 21px; border-radius: 3px; background: #4a78c2; display: block; }
  .social span + span { background: #6fb3e0; }

  .site-footer {
    left: 0; top: 1146px; width: 888px; height: 54px;
    background: linear-gradient(180deg, var(--magenta), var(--magenta-light));
  }
  .site-footer a { position: absolute; top: 16px; font-size: 9.5px; color: var(--white); }
</style>
</head>
<body>

<header class="site-header">
  <div class="brand-card"><span class="brand-dot"></span><span class="brand-name">FlockVault</span></div>
  <div class="abs headline">Get your favourite wine at discount prices</div>
  <nav class="main-nav">
    <a class="is-active" href="#" style="left:199px">Home</a>
    <a href="#" style="left:271px">Wine List</a>
    <a href="#" style="left:343px">About Us</a>
    <a href="#" style="left:415px">Register</a>
  </nav>
  <div class="abs login-bar">Login <span class="field">Username</span><span class="field">Password</span></div>
</header>

<section class="abs hero"></section>
<div class="abs community-art" role="img" aria-label="Illustration of a circle of wine club members linked together"></div>
<h1 class="abs hero-title">Connect,<br>Invite<br>and Buy</h1>
<p class="abs hero-lead">Join a family of wine enthusiasts and get the best experience out of your wine.</p>
<a class="abs btn-register" href="#">Register</a>

<svg class="abs carousel-arrow" style="left:147px;top:503px" viewBox="0 0 32 42" aria-label="Previous wine"><path d="M26 4 L8 21 L26 38" fill="none" stroke="#9ed04c" stroke-width="8" stroke-linecap="round" stroke-linejoin="round"/></svg>
<svg class="abs carousel-arrow" style="left:709px;top:522px" viewBox="0 0 32 42" aria-label="Next wine"><path d="M6 4 L24 21 L6 38" fill="none" stroke="#9ed04c" stroke-width="8" stroke-linecap="round" stroke-linejoin="round"/></svg>

<div class="abs bottle-photo" role="img" aria-label="Photo of the featured bottle of red wine"></div>

<div class="abs wine-name">Marlow</div>
<div class="abs wine-type">red wine</div>

<svg class="abs price-tag" width="134" height="84" viewBox="0 0 134 84" aria-hidden="true">
  <path d="M24 0 H130 a4 4 0 0 1 4 4 V80 a4 4 0 0 1 -4 4 H24 L0 62 V22 Z" fill="#8dc63f"/>
  <circle cx="23" cy="42" r="11" fill="#ffffff" opacity=".9"/>
  <circle cx="23" cy="42" r="6" fill="#8dc63f"/>
</svg>
<div class="abs price-was">$ 70 p/bottle</div>
<div class="abs price-label">Our Price</div>
<div class="abs price-now">$ 50</div>

<p class="abs wine-origin"><b>Made in</b> Lorem ipsum dolor sit amet, consectetur adipisicing elit, sed do eiusmod tempor incididunt ut labore et dolore magna aliqua. Ut enim ad minim veniam, quis nostrud exercitation ullamco laboris nisi ut aliquip ex ea commodo consequat.</p>

<div class="abs articles-link">
  <svg width="29" height="30" viewBox="0 0 29 30" aria-hidden="true"><path d="M3 8 L22 2 L27 22 L8 28 Z" fill="#f4f4f4" stroke="#c8c8c8"/></svg>
  <span>16 Articles</span>
</div>

<svg class="abs rating" width="165" height="28" viewBox="0 0 165 28" aria-label="Rated 4 out of 5">
  <defs><path id="star" d="M14 1 L17.5 10 L27 10.5 L19.5 16.5 L22 26 L14 20.5 L6 26 L8.5 16.5 L1 10.5 L10.5 10 Z"/></defs>
  <use href="#star" fill="#f7a11a"/>
  <use href="#star" x="32" fill="#f7a11a"/>
  <use href="#star" x="64" fill="#f7a11a"/>
  <use href="#star" x="96" fill="#f7a11a"/>
  <use href="#star" x="131" fill="#7d7d7d"/>
</svg>

<div class="abs meter-label">Buying meter</div>
<div class="abs buying-meter"><span></span></div>
<a class="abs btn-buy" href="#">Buy</a>

<div class="abs section-rule"></div>
<div class="abs tab-how">How it Works</div>

<article class="abs how-copy">
  <h2>Idus am sunditia aspelig enist, sus.</h2>
  <p>Vid qui arument landa pro ea dendi asit ex eos expere consecum et expliqu iberem aut veliquis et exerovi tatiosanis voluptio blametu repudiciis nihil mi, simporercid quae omnihil mollaccat lique modi restium et odioritaquam voluptat facim atiam et moluptatinus quatiisit dolecta volenducim utassitatem desti omnihit,</p>
  <p>adiorestrum acea venis et alibus et voluptatur serferumet molo culla quature omnihil intur? Qui blanihi citiass itiaecate sinihitatios dus raestisci autas atem faccatur aut minum am quid quia dolut eturerfero optatur aut ut delenim agnimpori quia que voluptatio ipid ma sitaqui rescide lictet ressequia delessequi ipsapel lacerepreped expe in nimosam nihicip iciaerspero eniet laces quatis erum doluptatem restrumquia nobitae nonsed que ero officil id quide non et atemper iossequ untorum fugitia poribus audigeni illa qui aliquidel idel et re quia volumque natis denis ma peliquae pe secea dendignis undiatur, qui unt, officabor sundis ape cum ut laborib usciur, cuscillant.</p>
  <p>Explit, voluptur, si dipsa voluptatur andae parum fugiatquiae sum eosti odis et volorem incia nihic te mo</p>
  <p>bea conecatat harum andae. Lore, vid quostrum nonsequ odionse quiaerruntis evellecatia non nonsequiae pro doluptatis duntior iatus, sundae dolupit atist, accum que pel inctis dollabore volo offictur molore</p>
</article>

<div class="abs social" aria-label="Social links"><span></span><span></span></div>

<footer class="abs site-footer">
  <a href="#" style="left:295px">Home</a>
  <a href="#" style="left:360px">Wine List</a>
  <a href="#" style="left:430px">About Us</a>
  <a href="#" style="left:502px">Register</a>
</footer>

</body>
</html>
```